Brennick Holdings Business Cards

These are professional business cards that are for my family office.
Put fake emails and phone numbers as of now until I finalize those components. This family office controls my families investments, assets, and future. The cards should be professional.
..
.
.
.
I just uploaded another variation of a logo I would like to see as a business card to I am inbeteen which logo to use

Target Market(s)

business

Industry/Entity Type

business

Contact Information for Business Card

Professional, wealth related, finance related.

Requirements
Must have
• Logo

```html
<!DOCTYPE html>
<html lang="en">
<head>
<meta charset="utf-8">
<title>Brennick Holdings Business Cards</title>
<link href="https://fonts.googleapis.com/css2?family=Cinzel:wght@500;600&family=Arimo:wght@400&display=swap" rel="stylesheet">
<style>
  :root {
    --backdrop: #3a3a3c;
    --navy: #1b1f2e;
    --navy-deep: #161a27;
    --paper: #ffffff;
    --rule-grey: #a9a9ad;
    --ink-light: #ffffff;
    --ink-muted: #c9ccd6;
  }
  * { margin: 0; padding: 0; box-sizing: border-box; }
  html, body { width: 1200px; height: 689px; overflow: hidden; }
  body {
    background: var(--backdrop);
    position: relative;
    font-family: "Arimo", Arial, sans-serif;
  }
  .card {
    position: absolute;
    top: 190px;
    width: 540px;
    height: 309px;
    border-radius: 18px;
    overflow: hidden;
    box-shadow: 0 14px 30px rgba(0,0,0,0.35);
  }
  /* Back of card */
  .card-back {
    left: 40px;
    background: var(--navy-deep);
  }
  .card-back .back-mark {
    position: absolute;
    top: 30px;
    right: 28px;
    display: flex;
    align-items: center;
    gap: 8px;
  }
  .back-mark .mark-circle {
    width: 22px; height: 22px;
    border: 1.5px solid var(--ink-light);
    border-radius: 50%;
  }
  .back-mark .mark-name {
    font-family: "Cinzel", Georgia, serif;
    font-weight: 500;
    font-size: 11px;
    color: var(--ink-light);
    letter-spacing: 0.5px;
  }
  /* Front of card */
  .card-front {
    left: 620px;
    background: var(--paper);
  }
  .card-front .curve-panel {
    position: absolute;
    inset: 0;
  }
  .brand {
    position: absolute;
    left: 34px;
    top: 92px;
    width: 240px;
    display: flex;
    flex-direction: column;
    align-items: center;
    gap: 14px;
  }
  .brand .brand-circle {
    width: 70px; height: 70px;
    border: 2.5px solid var(--navy);
    border-radius: 50%;
  }
  .brand .brand-name {
    font-family: "Cinzel", Georgia, serif;
    font-weight: 500;
    font-size: 22px;
    color: var(--navy);
    letter-spacing: 0.5px;
    white-space: nowrap;
  }
  .holder {
    position: absolute;
    right: 26px;
    top: 36px;
    text-align: right;
    color: var(--ink-light);
  }
  .holder .holder-name {
    font-family: "Cinzel", Georgia, serif;
    font-weight: 600;
    font-size: 20px;
    letter-spacing: 0.5px;
  }
  .holder .holder-title {
    font-size: 10px;
    margin-top: 1px;
  }
  .contact {
    position: absolute;
    right: 26px;
    top: 128px;
    text-align: right;
    color: var(--ink-light);
    font-size: 11.5px;
    line-height: 15px;
  }
  .contact .address { margin-bottom: 10px; padding-right: 20px; }
  .contact .row { display: flex; justify-content: flex-end; align-items: center; gap: 7px; }
  .contact .row svg { width: 12px; height: 12px; flex: none; }
</style>
</head>
<body>

<section class="card card-back" aria-label="Card back">
  <div class="back-mark">
    <span class="mark-circle"></span>
    <span class="mark-name">Brennick Holdings</span>
  </div>
</section>

<section class="card card-front" aria-label="Card front">
  <svg class="curve-panel" viewBox="0 0 540 309" preserveAspectRatio="none" aria-hidden="true">
    <path d="M362 0 C 300 70, 284 180, 300 309" fill="none" stroke="var(--rule-grey)" stroke-width="9"/>
    <path d="M374 0 C 314 70, 298 180, 314 309 L540 309 L540 0 Z" fill="var(--navy)"/>
  </svg>

  <div class="brand">
    <span class="brand-circle"></span>
    <span class="brand-name">Brennick Holdings</span>
  </div>

  <div class="holder">
    <div class="holder-name">Daniel Hart</div>
    <div class="holder-title">President</div>
  </div>

  <div class="contact">
    <div class="address">412 Alder Court<br>Halden, Canada 20418</div>
    <div class="row">555-201-4187
      <svg viewBox="0 0 12 12" aria-hidden="true"><path d="M2.5 1.5l2 .3.6 2.2-1.2.9a6 6 0 0 0 3.2 3.2l.9-1.2 2.2.6.3 2a1 1 0 0 1-1 1C5 10.5 1.5 7 1.5 2.5a1 1 0 0 1 1-1z" fill="var(--ink-light)"/></svg>
    </div>
    <div class="row">555-201-4392
      <svg viewBox="0 0 12 12" aria-hidden="true"><rect x="3" y="0.8" width="6" height="10.4" rx="1" fill="none" stroke="var(--ink-light)" stroke-width="1.2"/><circle cx="6" cy="9.4" r="0.6" fill="var(--ink-light)"/></svg>
    </div>
    <div class="row">info@brennickholdings.com
      <svg viewBox="0 0 12 12" aria-hidden="true"><rect x="0.8" y="2.5" width="10.4" height="7" fill="var(--ink-light)"/><path d="M0.8 2.5L6 6.5l5.2-4" fill="none" stroke="var(--navy)" stroke-width="1"/></svg>
    </div>
    <div class="row">www.brennickholdings.com
      <svg viewBox="0 0 12 12" aria-hidden="true"><circle cx="6" cy="6" r="5" fill="var(--ink-light)"/><path d="M1 6h10M6 1c-2 3-2 7 0 10M6 1c2 3 2 7 0 10" fill="none" stroke="var(--navy)" stroke-width="0.8"/></svg>
    </div>
  </div>
</section>

</body>
</html>
```